Business card for Mortgage broker business

I have already had the logo designed and am needing a great looking business card. My business focus is on servicing clients who may not be able to obtain finance through traditional lenders due to bad credit, short term employment or they just don't fit the banks profile. It needs to be professional, trust worthy but also have a caring fell about it.
I have provided files showing the green and black logo, the white logo(on white background so the file looks blank) and also a file with the white logo with a background of leaves that was made up which will probably be used for a website header.

Industry/Entity Type

Finance

Contact Information for Business Card

Marcus Dolbey
Managing Director, Accredited Finance Broker(AFB)
Po Box 287, Wattle Creek VIC 3819
marcus@kestrelfinance.com.au
www.kestrelfinance.com.au
0438 162 507

Requirements
Nice to have
• I have added a picture of myself as I would like to see some designs with the pic in it, but I'm not sure if I want it on there with the logo's or just the logo's

```html
<!DOCTYPE html>
<html lang="en">
<head>
<meta charset="utf-8">
<title>Kestrel Finance – Business Card</title>
<link href="https://fonts.googleapis.com/css2?family=Roboto:wght@400;500&display=swap" rel="stylesheet">
<style>
  :root {
    --bg: #e6e2dd;
    --card: #1b1b1b;
    --green: #0f7a3c;
    --white: #f2f2f2;
    --grey: #d6d6d6;
  }
  * { box-sizing: border-box; margin: 0; padding: 0; }
  html, body { width: 1200px; height: 864px; overflow: hidden; }
  body {
    background: var(--bg);
    font-family: "Roboto", Arial, sans-serif;
    display: flex;
    flex-direction: column;
    align-items: center;
    justify-content: center;
    gap: 40px;
  }
  .card {
    width: 620px;
    height: 354px;
    background: var(--card);
    border-radius: 4px;
    box-shadow: 0 10px 28px rgba(0,0,0,0.22);
    position: relative;
    color: var(--white);
  }
  .brand {
    display: flex;
    align-items: center;
    gap: 14px;
    color: var(--green);
    font-weight: 500;
    white-space: nowrap;
  }
  .brand-dot {
    width: 18px; height: 18px;
    border-radius: 50%;
    background: var(--green);
    flex: none;
  }

  /* Back side */
  .card-back {
    display: flex;
    flex-direction: column;
    align-items: center;
    justify-content: center;
    gap: 48px;
  }
  .card-back .brand-name { font-size: 54px; letter-spacing: 0.5px; }
  .web-line {
    font-size: 22px;
    font-weight: 500;
    letter-spacing: 0.5px;
    color: var(--white);
  }
  .web-line .accent { color: var(--green); }

  /* Front side */
  .card-front { padding: 0; }
  .front-logo {
    position: absolute;
    left: 44px;
    top: 52px;
  }
  .card-front .brand { gap: 10px; }
  .card-front .brand-name { font-size: 30px; }
  .card-front .brand-dot { width: 12px; height: 12px; }
  .divider {
    position: absolute;
    left: 300px;
    top: 120px;
    width: 1px;
    height: 190px;
    background: var(--grey);
  }
  .details {
    position: absolute;
    left: 330px;
    top: 150px;
    display: flex;
    flex-direction: column;
    white-space: nowrap;
  }
  .person-name { font-size: 28px; font-weight: 500; color: var(--white); }
  .person-title { font-size: 16px; color: var(--green); margin: 4px 0 16px; }
  .contact-list { list-style: none; font-size: 15px; line-height: 1.45; color: var(--white); }
  .contact-list li { display: flex; align-items: center; gap: 8px; }
  .contact-list li.plain { padding-left: 20px; }
  .icon { width: 12px; height: 12px; flex: none; }
</style>
</head>
<body>

  <section class="card card-back" aria-label="Card back">
    <div class="brand">
      <span class="brand-dot"></span>
      <span class="brand-name">Kestrel Finance</span>
    </div>
    <p class="web-line">WWW.<span class="accent">KESTRELFINANCE.COM.AU</span></p>
  </section>

  <section class="card card-front" aria-label="Card front">
    <div class="front-logo">
      <div class="brand">
        <span class="brand-dot"></span>
        <span class="brand-name">Kestrel Finance</span>
      </div>
    </div>
    <div class="divider"></div>
    <div class="details">
      <h1 class="person-name">Marcus Dolbey</h1>
      <p class="person-title">Managing Director (AFB)</p>
      <ul class="contact-list">
        <li class="plain">Po Box 287</li>
        <li class="plain">Wattle Creek VIC 3819</li>
        <li>
          <svg class="icon" viewBox="0 0 12 12" aria-hidden="true"><rect x="0.5" y="2" width="11" height="8" rx="1" fill="var(--green)"/><path d="M1 2.8 6 6.6 11 2.8" stroke="#1b1b1b" stroke-width="1" fill="none"/></svg>
          marcus@kestrelfinance.com.au
        </li>
        <li>
          <svg class="icon" viewBox="0 0 12 12" aria-hidden="true"><circle cx="6" cy="6" r="5.5" fill="var(--green)"/><path d="M0.8 6h10.4M6 0.8c-2.4 3-2.4 7.4 0 10.4M6 0.8c2.4 3 2.4 7.4 0 10.4" stroke="#1b1b1b" stroke-width="0.8" fill="none"/></svg>
          www.kestrelfinance.com.au
        </li>
      </ul>
    </div>
  </section>

</body>
</html>
```